Pellora Networks web design

Pellora is an Internet Service Provider bringing high-speed service to homes and businesses. Our principal market target is rural areas of West Michigan, but we intend to expand rapidly. We need a website to market our services, facilitate online ordering, customer support and communicate with our customers.

I will upload a draft outline of the content we hope to include in the website.

We compete directly with Bramwell Communications, Quendar, Lumitek and Hollister communications to bring Internet service to homes and businesses in our coverage area.

Our primary values include:

1. Unlike our competitors, we do not require long term contractors or service bundles; There are no termination fees, for example. All services are sold on a recurring 1-month agreement term.
2. Unlike other wireless (mobile) providers, we do not limit downloads or uploads with bit/byte buckets
3. We provide service to areas ignored by the larger carriers - Rural areas in Michigan that lack options for broadband are prime targets for Pellora to cover.
4. Unlike other wireless ISP's, we utilize licensed FCC spectrum. We do not use unlicensed/free frequencies, providing us an advantage for reliability and stability.

So many wonderful designs, thank you very much for all your hard work. We are evaluating all our favorite designs and plan to make a selection in the next 2 days. I will be in touch with you to request revisions if necessary or further refinements.  Thank you again for your efforts on this project.

Target Market(s)

Our target market is home Internet users. however, that does not mean that our users are "high tech" oriented - they are just normal mom's and pop's who buy Internet for home use. The site should be easy to navigate and communicate our message of speed, value, reliability and facilitate simple product ordering.

Industry/Entity Type

Internet

Requirements
Must have
• Our phone number should be prominently displayed 1-844-7RU-NLOK
• Our logo is uploaded in the attachments.
• Design for desktop and mobile devices.
Nice to have
• The most modern of web design trends. Such as a design that facilitates parallax scrolling effects rather than lots of individual pages.
• Stock artwork communicating our values of speed and reliability.

```html
<!DOCTYPE html>
<html lang="en">
<head>
<meta charset="utf-8">
<title>Pellora Networks — West Michigan's Best Internet Service</title>
<link href="https://fonts.googleapis.com/css2?family=Roboto:wght@300;400;500;700;900&display=swap" rel="stylesheet">
<style>
  :root {
    --orange: #f57c00;
    --orange-soft: #f7931e;
    --hero-bg: #4a4a4a;
    --hero-dark: #3d3d3d;
    --ink: #333333;
    --ink-soft: #777777;
    --rule: #e3e3e3;
    --white: #ffffff;
    --map-land: #8e8e8e;
    --map-water: #5a5a5a;
    --footer-bg: #555555;
    --footer-text: #c9c9c9;
  }
  * { box-sizing: border-box; margin: 0; padding: 0; }
  html, body { width: 1200px; height: 2500px; overflow: hidden; }
  body { font-family: "Roboto", Arial, sans-serif; color: var(--ink); background: var(--white); position: relative; }
  .abs { position: absolute; }

  /* Hero */
  .hero { position: absolute; left: 0; top: 0; width: 1200px; height: 487px;
    background: linear-gradient(135deg, var(--hero-bg) 0%, #525252 45%, var(--hero-dark) 100%); }
  .site-header { position: absolute; left: 244px; top: 0; width: 956px; height: 80px; background: var(--white);
    display: flex; align-items: center; padding-left: 48px; }
  .brand { display: flex; align-items: center; gap: 10px; width: 196px; }
  .brand-dot { width: 14px; height: 14px; border-radius: 50%; background: var(--orange); }
  .brand-name { font-weight: 900; font-size: 22px; line-height: 1; color: var(--orange); letter-spacing: 0.5px; }
  .brand-name small { display: block; font-size: 11px; letter-spacing: 4px; }
  .tagline { font-size: 16px; color: var(--ink); padding-left: 22px; }
  .header-rule { width: 1px; height: 52px; background: var(--rule); margin-left: 30px; }
  .phone { display: flex; align-items: center; gap: 8px; margin-left: 24px; color: var(--orange); font-size: 19px; font-weight: 300; }

  .main-nav { position: absolute; left: 293px; top: 92px; display: flex; gap: 20px; font-size: 10px; font-weight: 500; color: var(--white); text-transform: uppercase; }
  .main-nav .is-active { border-bottom: 2px solid var(--orange); padding-bottom: 6px; }
  .nav-search { position: absolute; left: 893px; top: 92px; }
  .nav-rule { position: absolute; left: 0; top: 126px; width: 1200px; height: 1px; background: rgba(255,255,255,0.18); }

  .hero-title { position: absolute; left: 293px; top: 160px; font-size: 46px; font-weight: 900; color: var(--white); letter-spacing: -0.5px; }
  .timeline { position: absolute; left: 244px; top: 270px; width: 712px; height: 2px; background: var(--orange); }
  .feature-icon { position: absolute; top: 248px; width: 46px; height: 46px; border-radius: 50%; background: var(--orange); display: flex; align-items: center; justify-content: center; }
  .feature { position: absolute; top: 312px; width: 270px; }
  .feature h3 { font-size: 17px; font-weight: 400; color: var(--white); margin-bottom: 14px; }
  .feature p { font-size: 11.5px; line-height: 1.45; color: var(--orange-soft); }
  .slide-arrow { position: absolute; top: 270px; width: 40px; height: 40px; border: 1.5px solid rgba(255,255,255,0.8); border-radius: 50%; display: flex; align-items: center; justify-content: center; }
  .slide-dots { position: absolute; left: 293px; top: 500px; display: flex; gap: 5px; }
  .slide-dots span { width: 5px; height: 5px; border-radius: 50%; background: #cfcfcf; }
  .slide-dots span:first-child { background: #888; }

  /* Plans */
  .section-title { position: absolute; left: 0; width: 1200px; text-align: center; font-weight: 300; font-size: 38px; }
  .plans-title { top: 668px; color: var(--orange-soft); }
  .plan-tabs { position: absolute; left: 450px; top: 742px; width: 300px; height: 40px; display: flex; border: 1px solid #cfcfcf; border-radius: 3px; }
  .plan-tabs div { flex: 1; display: flex; align-items: center; justify-content: center; font-size: 14px; color: #999; }
  .plan-tabs .is-active { color: var(--ink); border: 2px solid #bdbdbd; border-radius: 3px; background: #fafafa; }

  .plan-table { position: absolute; left: 244px; top: 820px; width: 712px; }
  .plan-row-rule { position: absolute; height: 1px; background: var(--rule); }
  .col-rule { position: absolute; width: 1px; background: var(--rule); }
  .plan-name { position: absolute; width: 200px; text-align: center; font-size: 16px; font-weight: 300; color: #888; }
  .plan-name.is-featured { font-size: 19px; font-weight: 400; color: var(--ink); }
  .plan-speed { position: absolute; width: 200px; text-align: center; font-size: 11px; line-height: 20px; color: var(--ink-soft); }
  .plan-speed em { font-style: normal; color: var(--orange-soft); }
  .plan-common { position: absolute; left: 0; width: 712px; text-align: center; font-size: 12.5px; color: var(--ink-soft); }
  .plan-price { position: absolute; width: 200px; text-align: center; color: var(--orange); font-size: 32px; font-weight: 300; }
  .plan-price sup { font-size: 16px; vertical-align: 14px; }
  .plan-price small { font-size: 9px; color: #aaa; }
  .price-rule { position: absolute; width: 40px; height: 3px; background: #d8d8d8; }
  .plan-install { position: absolute; width: 200px; text-align: center; font-size: 17px; font-weight: 300; color: var(--ink); }
  .plan-install sup { font-size: 9px; }
  .order-btn { position: absolute; width: 114px; height: 34px; border: 2px solid var(--orange); border-radius: 6px; color: var(--orange); font-size: 10px; font-weight: 700; display: flex; align-items: center; justify-content: center; }
  .order-btn.is-filled { background: var(--orange); color: var(--white); }
  .plan-options { position: absolute; left: 356px; top: 1225px; width: 488px; height: 45px; border: 1px solid #d6d6d6; border-radius: 4px; display: flex; align-items: center; justify-content: center; font-size: 12.5px; color: var(--ink); }
  .plan-options strong { font-weight: 500; margin-right: 4px; }
  .plan-options em { font-style: normal; color: var(--orange); margin: 0 4px; }

  /* Coverage */
  .coverage-title { top: 1414px; color: #5a5a5a; }
  .coverage-map { position: absolute; left: 0; top: 1479px; width: 1200px; height: 438px;
    background: radial-gradient(ellipse at 30% 60%, var(--map-land) 0%, #7e7e7e 55%, var(--map-water) 100%); }
  .coverage-search { position: absolute; left: 356px; top: 1500px; width: 488px; height: 42px; background: #2b2b2b; border-radius: 4px; display: flex; align-items: center; padding-left: 16px; gap: 12px; font-size: 11px; color: #9a9a9a; }
  .coverage-search .search-btn { position: absolute; right: 0; top: 0; width: 42px; height: 42px; background: var(--orange); border-radius: 0 4px 4px 0; display: flex; align-items: center; justify-content: center; }
  .coverage-order { position: absolute; left: 521px; top: 1824px; width: 158px; height: 44px; background: var(--orange); border-radius: 4px; color: var(--white); font-size: 17px; display: flex; align-items: center; justify-content: center; }

  /* Footer */
  .site-footer { position: absolute; left: 0; top: 1917px; width: 1200px; height: 583px; background: var(--footer-bg); color: var(--footer-text); }
  .contact-title { position: absolute; left: 293px; top: 44px; font-size: 27px; font-weight: 900; color: var(--white); }
  .contact-title::after { content: ""; display: block; width: 122px; height: 3px; background: var(--orange); margin-top: 8px; }
  .contact-block { position: absolute; font-size: 11px; line-height: 16px; text-transform: uppercase; }
  .contact-block strong { color: var(--white); font-weight: 700; }
  .contact-block .accent { color: var(--orange-soft); font-weight: 700; }
  .contact-block .email { color: var(--orange-soft); font-weight: 700; border-bottom: 2px solid var(--orange); padding-bottom: 3px; }
  .contact-block h4 { color: var(--white); font-size: 11.5px; font-weight: 700; margin-bottom: 10px; }
  .footer-nav { position: absolute; left: 293px; top: 383px; display: flex; gap: 10px; font-size: 10px; color: var(--footer-text); }
  .footer-nav .is-active { color: var(--white); font-weight: 700; border-bottom: 2px solid var(--orange); padding-bottom: 6px; }
  .footer-nav i { font-style: normal; color: #888; }
  .footer-rule { position: absolute; left: 293px; top: 410px; width: 664px; height: 1px; background: #707070; }
  .copyright { position: absolute; left: 0; width: 1200px; text-align: center; font-size: 9.5px; color: #aaa; }
  .copyright b { color: var(--white); font-weight: 400; }
  .footer-brand { position: absolute; left: 0; top: 488px; width: 1200px; text-align: center; font-weight: 900; font-size: 16px; color: #7a7a7a; letter-spacing: 1px; line-height: 1; }
  .footer-brand small { display: block; font-size: 8px; letter-spacing: 3px; }
</style>
</head>
<body>

<section class="hero" role="img" aria-label="Dark grey faceted abstract background">
  <header class="site-header">
    <div class="brand">
      <span class="brand-dot"></span>
      <div class="brand-name">PELLORA<small>NETWORKS</small></div>
    </div>
    <div class="tagline">West Michigan's Best Internet Service</div>
    <div class="header-rule"></div>
    <div class="phone">
      <svg width="16" height="16" viewBox="0 0 24 24" fill="none" stroke="#f57c00" stroke-width="2"><path d="M5 3h4l2 5-3 2a12 12 0 0 0 6 6l2-3 5 2v4a2 2 0 0 1-2 2A17 17 0 0 1 3 5a2 2 0 0 1 2-2z"/></svg>
      1-844-7RU-NLOK
    </div>
  </header>

  <nav class="main-nav">
    <span class="is-active">Home</span><span>Service Plans</span><span>Coverage</span><span>Who's Pellora</span><span>Blog</span><span>Support</span><span>Contact Us</span>
  </nav>
  <svg class="nav-search" width="14" height="14" viewBox="0 0 24 24" fill="none" stroke="#fff" stroke-width="3"><circle cx="10" cy="10" r="7"/><path d="M15 15l6 6"/></svg>
  <div class="nav-rule"></div>

  <h1 class="hero-title">BUY LOCAL!</h1>
  <div class="timeline"></div>

  <div class="feature-icon" style="left:294px">
    <svg width="20" height="20" viewBox="0 0 24 24" fill="none" stroke="#fff" stroke-width="2"><path d="M12 22s7-7 7-12a7 7 0 0 0-14 0c0 5 7 12 7 12z"/><circle cx="12" cy="10" r="2.5"/></svg>
  </div>
  <div class="feature-icon" style="left:608px">
    <svg width="20" height="20" viewBox="0 0 24 24" fill="none" stroke="#fff" stroke-width="2"><path d="M12 3l2.8 5.8 6.2.9-4.5 4.4 1 6.2L12 17.4 6.5 20.3l1-6.2L3 9.7l6.2-.9z"/></svg>
  </div>

  <div class="feature" style="left:293px">
    <h3>Pellora is Local!</h3>
    <p>We're a locally owned and operated business. All of our staff live and work in Michigan. We re-invest in our local community because we live it - just like you!</p>
  </div>
  <div class="feature" style="left:606px">
    <h3>Best Value, Best for You!</h3>
    <p>Unlike cable and phone companies, we don't require you to buy everything from us. We offer the best value Internet service, and only what you want, no "bundles" required.</p>
  </div>

  <div class="slide-arrow" style="left:61px">
    <svg width="10" height="10" viewBox="0 0 10 10" fill="none" stroke="#fff" stroke-width="1.5"><path d="M6.5 1.5L3 5l3.5 3.5"/></svg>
  </div>
  <div class="slide-arrow" style="left:1097px">
    <svg width="10" height="10" viewBox="0 0 10 10" fill="none" stroke="#fff" stroke-width="1.5"><path d="M3.5 1.5L7 5 3.5 8.5"/></svg>
  </div>
</section>
<div class="slide-dots"><span></span><span></span><span></span></div>

<section class="plans">
  <h2 class="section-title plans-title">SERVICE PLANS</h2>
  <div class="plan-tabs"><div class="is-active">RESIDENTIAL</div><div>BUSINESS</div></div>

  <div class="plan-table">
    <div class="plan-row-rule" style="left:0;top:42px;width:712px"></div>
    <div class="col-rule" style="left:256px;top:0;height:122px"></div>
    <div class="col-rule" style="left:456px;top:0;height:122px"></div>
    <div class="plan-row-rule" style="left:0;top:122px;width:712px"></div>

    <div class="plan-name" style="left:56px;top:16px">Best Value</div>
    <div class="plan-name is-featured" style="left:256px;top:12px">Premium Value</div>
    <div class="plan-name" style="left:456px;top:16px">Unlimited</div>

    <div class="plan-speed" style="left:56px;top:68px">Up to <em>1.0 Mb</em> Download<br><em>512 Kbs</em> Upload</div>
    <div class="plan-speed" style="left:256px;top:68px">Up to <em>3.0 Mb</em> Download<br><em>1.0 Mb</em> Upload</div>
    <div class="plan-speed" style="left:456px;top:68px">Up to <em>10.0 Mb</em> Download<br><em>2.0 Mb</em> Upload</div>

    <div class="plan-common" style="top:140px">Unlimited download and upload - ie; "no bit buckets"</div>
    <div class="plan-common" style="top:167px">Up to 5 Mailstead enabled email accounts</div>
    <div class="plan-row-rule" style="left:66px;top:202px;width:580px"></div>
    <div class="col-rule" style="left:256px;top:202px;height:176px"></div>
    <div class="col-rule" style="left:456px;top:202px;height:176px"></div>

    <div class="plan-price" style="left:56px;top:222px">$24<sup>99</sup> <small>/mo</small></div>
    <div class="plan-price" style="left:256px;top:222px">$44<sup>99</sup> <small>/mo</small></div>
    <div class="plan-price" style="left:456px;top:222px">$74<sup>99</sup> <small>/mo</small></div>
    <div class="price-rule" style="left:136px;top:268px"></div>
    <div class="price-rule" style="left:336px;top:268px"></div>
    <div class="price-rule" style="left:536px;top:268px"></div>

    <div class="plan-install" style="left:56px;top:282px">$100<sup>00</sup> Install</div>
    <div class="plan-install" style="left:256px;top:282px">$100<sup>00</sup> Install</div>
    <div class="plan-install" style="left:456px;top:282px">$100<sup>00</sup> Install</div>

    <div class="order-btn" style="left:99px;top:321px">ORDER NOW</div>
    <div class="order-btn is-filled" style="left:299px;top:321px">ORDER NOW</div>
    <div class="order-btn" style="left:499px;top:321px">ORDER NOW</div>
  </div>

  <div class="plan-options"><strong>Optional services:</strong> Static IP address <em>$15.00</em> each /month</div>
</section>

<section class="coverage">
  <h2 class="section-title coverage-title">AM I COVERED?</h2>
  <div class="coverage-map" role="img" aria-label="Grey map of West Michigan showing the service coverage area"></div>
  <div class="coverage-search">
    <svg width="14" height="14" viewBox="0 0 24 24" fill="none" stroke="#ccc" stroke-width="2"><path d="M12 22s7-7 7-12a7 7 0 0 0-14 0c0 5 7 12 7 12z"/><circle cx="12" cy="10" r="2.5"/></svg>
    Enter your address to check for service availability
    <div class="search-btn">
      <svg width="16" height="16" viewBox="0 0 24 24" fill="none" stroke="#fff" stroke-width="3"><circle cx="10" cy="10" r="6.5"/><path d="M15 15l6 6"/></svg>
    </div>
  </div>
  <div class="coverage-order">ORDER NOW!</div>
</section>

<footer class="site-footer">
  <h2 class="contact-title">CONTACT</h2>

  <div class="contact-block" style="left:293px;top:117px;width:270px">
    Call today to place an order or reach customer support <strong>844-7RU-NLOK</strong><br><br>
    Local number: <strong>517-555-0143</strong><br><br>
    Email support: <span class="email">support@pellorafast.net</span>
  </div>

  <div class="contact-block" style="left:644px;top:117px;width:260px">
    <h4>SUPPORT STAFF HOURS</h4>
    Weekdays &nbsp;&nbsp;<span class="accent">7AM TO 10PM</span><br>
    Weekends &nbsp;&nbsp;<span class="accent">8AM TO 5PM</span><br>
    Holiday scheduling varies
  </div>

  <div class="contact-block" style="left:644px;top:228px;width:260px">
    <h4 style="margin-bottom:4px">PELLORA NETWORKS</h4>
    LLC 2710 Harlow Avenue<br>Elm Rapids,<br>MI 49901
  </div>

  <nav class="footer-nav">
    <span class="is-active">Home</span><i>/</i><span>Service Plans</span><i>/</i><span>Coverage Map</span><i>/</i><span>Who's Pellora</span><i>/</i><span>Company Blog</span><i>/</i><span>Customer Support</span><i>/</i><span>Account Management</span>
  </nav>
  <div class="footer-rule"></div>

  <div class="copyright" style="top:437px">Copyright 2014 <b>Pellora Networks</b> LLC All Rights Reserved</div>
  <div class="copyright" style="top:455px">Proudly built and hosted in Michigan ♡</div>
  <div class="footer-brand">PELLORA<small>NETWORKS</small></div>
</footer>

</body>
</html>
```